Pregnancy Wellbeing Coach seeks Book Cover Design

I am a former midwife who now works within alternative healthcare to support women and their families during pregnancy.
I have written a book "Quiet and Carrying Light" which is a pregnancy guide that encourages women to look "outside the box" of conventional medicine ...to find alternative solutions to difficulties that they might be experiencing. So it looks as breathing, meditative and journeying techniques, exercise, connection to nature, communication with the baby...those sort of things.
The book also is a guide for those who support the pregnant women ...the best friend, sister, mother, partner - all those who want to be involved and make a positive contribution to the transformation of the woman into motherhood ...because undoubtedly their lives will be changed by the experience.
It is my belief that we all hold an innate wisdom, the wisdom of our ancestors and that during pregnancy women are connected to the lineage of child bearers back through time ...so it is has a sacred element to it, a time of coming together ... a passing through a doorway, where life will be forever changed.
My website is : www.maevelorrimerwellbeing.example

Thank you :)

Target Market(s)

Pregnant women and those who support them during pregnancy

Industry/Entity Type

Health Care

Font styles to use
Serif
Script

Colors

Designer to choose colors to be used in the design.

Requirements
Must have
• A pregnant woman ...
• Natural World
• Title : Quiet & Carrying Light
• Subtitle : Gentle Practices to Guide A Present-Day Mother's Changing Passage Across the Months of Waiting
• Author: Maeve Lorrimer
Nice to have
• I have a feeling that nature or the natural world is important.
• And the sign of support/community
• And maybe the stars
Should not have
• No Babies
• No "highly polished women"
• No huge pregnant bellies

```html
<!DOCTYPE html>
<html lang="en">
<head>
<meta charset="utf-8">
<title>Quiet &amp; Carrying Light — Book Cover</title>
<link rel="stylesheet" href="https://fonts.googleapis.com/css2?family=Playfair+Display:wght@700;900&family=Open+Sans:wght@400;700&display=swap">
<style>
  :root {
    --page: #ffffff;
    --night: #1c4aa3;
    --sky: #6f9fd6;
    --sky-pale: #b9d5ee;
    --haze: #eef3f6;
    --sea: #9dbccc;
    --sea-deep: #6f93a8;
    --sand: #cdbba3;
    --sand-dark: #b39e84;
    --title-light: #ffffff;
    --ink: #111111;
  }
  * { margin: 0; padding: 0; box-sizing: border-box; }
  html, body {
    width: 1200px;
    height: 1200px;
    overflow: hidden;
    background: var(--page);
  }
  .canvas {
    position: relative;
    width: 1200px;
    height: 1200px;
  }
  .cover {
    position: absolute;
    left: 236px;
    top: 85px;
    width: 745px;
    height: 1040px;
    overflow: hidden;
  }
  .cover-scene {
    position: absolute;
    inset: 0;
    background:
      radial-gradient(ellipse 40% 8% at 30% 84%, rgba(255,255,255,0.55), transparent 70%),
      linear-gradient(180deg,
        var(--night) 0%,
        var(--sky) 22%,
        var(--sky-pale) 42%,
        var(--haze) 62%,
        var(--haze) 72%,
        var(--sea) 80%,
        var(--sea-deep) 83%,
        var(--sand) 88%,
        var(--sand-dark) 100%);
  }
  .cover-text {
    position: absolute;
    inset: 0;
    text-align: center;
  }
  .title-main {
    position: absolute;
    left: 0;
    right: 0;
    top: 52px;
    font-family: "Playfair Display", Georgia, serif;
    font-weight: 900;
    font-size: 206px;
    line-height: 1;
    color: var(--title-light);
    letter-spacing: -2px;
  }
  .title-amp {
    position: absolute;
    left: 0;
    right: 0;
    top: 288px;
    font-family: "Playfair Display", Georgia, serif;
    font-weight: 900;
    font-size: 54px;
    line-height: 1;
    color: var(--ink);
  }
  .title-second {
    position: absolute;
    left: 0;
    right: 0;
    top: 338px;
    font-family: "Playfair Display", Georgia, serif;
    font-weight: 900;
    font-size: 62px;
    line-height: 1;
    color: var(--ink);
    letter-spacing: -1px;
  }
  .subtitle-block {
    position: absolute;
    left: 40px;
    right: 40px;
    top: 546px;
  }
  .rule {
    display: block;
    width: 273px;
    height: 2px;
    margin: 0 auto;
    background: var(--ink);
  }
  .subtitle {
    margin: 14px 0 16px;
    font-family: "Open Sans", Arial, sans-serif;
    font-weight: 400;
    font-size: 25px;
    line-height: 37px;
    color: var(--ink);
  }
  .author {
    position: absolute;
    left: 0;
    right: 0;
    top: 978px;
    font-family: "Open Sans", Arial, sans-serif;
    font-weight: 700;
    font-size: 40px;
    line-height: 1;
    color: var(--ink);
  }
</style>
</head>
<body>
  <div class="canvas">
    <div class="cover">
      <div class="cover-scene" role="img" aria-label="Photograph of a starry blue twilight sky over a quiet beach, with a pregnant woman in a flowing turquoise dress standing barefoot at the water's edge"></div>
      <div class="cover-text">
        <h1 class="title-main">QUIET</h1>
        <div class="title-amp">&amp;</div>
        <div class="title-second">CARRYING LIGHT</div>
        <div class="subtitle-block">
          <span class="rule"></span>
          <p class="subtitle">Gentle Practices to Guide A Present-Day Mother's<br>Changing Passage Across the Months of Waiting</p>
          <span class="rule"></span>
        </div>
        <div class="author">MAEVE LORRIMER</div>
      </div>
    </div>
  </div>
</body>
</html>
```